Dana's Business Card Design

I am in need of a business card design for our company Tolleshunt Wrecking & Reclaim (WA) Pty Ltd. Apart from being licenced demolition contractors for residential, commercial or industrial projects we have a 20 acre salvage yard full of recycled building materials, we are also licenced to remove Asbestos and we have our own recycling/refuge tip and this site is also licenced to take Asbestos contamination landfill,we also have a sandpit in which we sell sand. Our primary colour is blue and we have a little man logo which i will attach that has been our logo for the good part of the last thirty years so this is to be included, I wont mind if you alter/update him in any way although his tattoo's must remain.
Target Market(s)
Construction & Building Industry
Industry/Entity Type
Industrial
Contact Information for Business Card
TOLLESHUNT WRECKING & RECLAIM (WA) PTY LTD
Dana Tolleshunt
Credit Controller/Payroll Officer
2417 Felmore Ridge Road
LOWER ELDERGATE  WA  6071
PH: 0428 615 704
Fax: (08) 9371 5820
dana@twreck.example.com.au
tolleshuntwrecking.example.com.au

```html
<!DOCTYPE html>
<html lang="en">
<head>
<meta charset="utf-8">
<title>Dana Tolleshunt – Business Card</title>
<link rel="stylesheet" href="https://fonts.googleapis.com/css2?family=Lato:wght@400;700;900&display=swap">
<style>
  :root {
    --brand-blue: #1e9fd8;
    --bubble-blue: #1a8cc9;
    --ink: #222a30;
    --rule: #2b2f33;
    --card: #ffffff;
    --page: #e9ebee;
    --figure-a: #5a6bb0;
    --figure-b: #c9a07a;
  }
  * { box-sizing: border-box; margin: 0; padding: 0; }
  html, body { width: 1200px; height: 926px; overflow: hidden; }
  body {
    background: var(--page);
    font-family: "Lato", Arial, sans-serif;
    display: flex; align-items: center; justify-content: center;
  }
  .business-card {
    position: relative;
    width: 1000px; height: 572px;
    background: var(--card);
    border: 14px solid var(--brand-blue);
    box-shadow: 0 10px 30px rgba(0,0,0,.15);
  }
  .mascot {
    position: absolute; left: 46px; top: 118px;
    width: 160px; height: 220px;
    border-radius: 40px 40px 16px 16px;
    background: linear-gradient(180deg, var(--figure-a) 0%, var(--figure-a) 60%, var(--figure-b) 100%);
  }
  .company-bubble {
    position: absolute; left: 214px; top: 50px;
    width: 300px; height: 96px;
    background: var(--bubble-blue);
    color: #fff;
    font-weight: 700; font-size: 21px; line-height: 1.25;
    padding: 20px 22px;
    clip-path: polygon(0 0, 100% 0, 100% 82%, 94% 100%, 0 100%);
  }
  .bubble-tail { position: absolute; left: 176px; top: 120px; }
  .identity { position: absolute; left: 560px; top: 84px; }
  .person-name {
    color: var(--brand-blue);
    font-weight: 900; font-size: 34px; letter-spacing: 1px;
  }
  .person-role { color: var(--ink); font-weight: 700; font-size: 19px; margin-top: 0; }
  .contact-list { position: absolute; left: 540px; top: 176px; width: 400px; list-style: none; }
  .contact-item {
    height: 62px;
    border-bottom: 2px solid var(--rule);
    margin-bottom: 8px;
    padding-top: 4px;
    color: var(--ink); font-size: 19px;
  }
  .contact-item svg { display: block; margin-bottom: 4px; }
  .address {
    position: absolute; left: 36px; bottom: 40px;
    display: flex; align-items: center; gap: 14px;
    color: var(--ink); font-size: 25px; letter-spacing: 2.5px;
  }
</style>
</head>
<body>
  <article class="business-card">
    <div class="mascot" role="img" aria-label="Company mascot: a tattooed demolition worker in a hard hat holding a shovel"></div>

    <svg class="bubble-tail" width="44" height="30" viewBox="0 0 44 30" aria-hidden="true">
      <polygon points="44,0 44,18 0,30" fill="var(--bubble-blue)"/>
    </svg>
    <div class="company-bubble">Tolleshunt Wrecking<br>&amp; Reclaim (WA) Pty Ltd</div>

    <header class="identity">
      <h1 class="person-name">DANA TOLLESHUNT</h1>
      <p class="person-role">Credit Controller/Payroll Officer</p>
    </header>

    <ul class="contact-list">
      <li class="contact-item">
        <svg width="20" height="14" viewBox="0 0 20 14" aria-hidden="true"><rect x="1" y="1" width="18" height="12" fill="none" stroke="var(--brand-blue)" stroke-width="2"/><path d="M1 1 L10 8 L19 1" fill="none" stroke="var(--brand-blue)" stroke-width="2"/></svg>
        dana@twreck.example.com.au
      </li>
      <li class="contact-item">
        <svg width="16" height="18" viewBox="0 0 16 18" aria-hidden="true"><rect x="2" y="1" width="12" height="16" rx="2" fill="none" stroke="var(--brand-blue)" stroke-width="2"/><rect x="5" y="13" width="6" height="2" fill="var(--brand-blue)"/></svg>
        0428 615 704
      </li>
      <li class="contact-item">
        <svg width="20" height="18" viewBox="0 0 20 18" aria-hidden="true"><rect x="5" y="1" width="10" height="6" fill="none" stroke="var(--brand-blue)" stroke-width="2"/><rect x="1" y="7" width="18" height="10" fill="var(--brand-blue)"/><rect x="5" y="11" width="10" height="2" fill="#fff"/></svg>
        (08) 9371 5820
      </li>
      <li class="contact-item">
        <svg width="22" height="18" viewBox="0 0 22 18" aria-hidden="true"><rect x="1" y="1" width="20" height="12" fill="none" stroke="var(--brand-blue)" stroke-width="2"/><rect x="7" y="15" width="8" height="2" fill="var(--brand-blue)"/></svg>
        tolleshuntwrecking.example.com.au
      </li>
    </ul>

    <p class="address">
      <svg width="18" height="24" viewBox="0 0 18 24" aria-hidden="true"><path d="M9 1 C4.5 1 1 4.5 1 9 C1 15 9 23 9 23 C9 23 17 15 17 9 C17 4.5 13.5 1 9 1 Z" fill="none" stroke="var(--brand-blue)" stroke-width="2.5"/><circle cx="9" cy="9" r="3" fill="var(--brand-blue)"/></svg>
      2417 Felmore Ridge Road, LOWER ELDERGATE, WA 6071
    </p>
  </article>
</body>
</html>
```